Brightfield Athletics and fitness is Hosting a Spring Renewal yoga class. World-renowned Tobe Garrowen will be teaching. Tobe is a Life Empowerment Coach. This event will take place on January 5th, 2019 Time: 2pm - 4pmYoga at Optimum Sports and FitnessCost: $30 / $40 at the Door

Requirements
Must have
• Brightfield Athletics and fitness Logo
• Brightfield Lantern Yoga Logo

```html
<!DOCTYPE html>
<html lang="en">
<head>
<meta charset="utf-8">
<title>Spring Renewal Yoga Class</title>
<link rel="stylesheet" href="https://fonts.googleapis.com/css2?family=Arimo:wght@400;700&family=Tinos:wght@700&display=swap">
<style>
  :root {
    --stage: #2a2829;
    --ink: #000000;
    --white: #ffffff;
    --red: #e31e24;
    --red-deep: #9c151b;
    --red-soft: #e2343b;
    --photo-light: #c9c9c9;
    --photo-mid: #8c8c8c;
    --photo-dark: #4a4a4a;
    --icon-grey: #7a7a7a;
  }
  html, body {
    margin: 0;
    width: 1200px;
    height: 1200px;
    overflow: hidden;
    background: var(--stage);
  }
  .flyer {
    position: absolute;
    left: 200px;
    top: 34px;
    width: 800px;
    height: 1131px;
    display: block;
  }
  .serif { font-family: "Tinos", "Times New Roman", serif; font-weight: 700; }
  .sans { font-family: "Arimo", Arial, sans-serif; font-weight: 700; }
  .brand-name { font-family: "Arimo", Arial, sans-serif; font-weight: 400; }
</style>
</head>
<body>
<svg class="flyer" viewBox="0 0 925 1308" xmlns="http://www.w3.org/2000/svg">
  <defs>
    <linearGradient id="backdrop-tone" x1="0" y1="0" x2="1" y2="1">
      <stop offset="0" stop-color="var(--photo-light)"/>
      <stop offset="0.5" stop-color="var(--photo-mid)"/>
      <stop offset="1" stop-color="var(--photo-dark)"/>
    </linearGradient>
    <radialGradient id="portrait-tone" cx="0.5" cy="0.45" r="0.6">
      <stop offset="0" stop-color="#9a9a9a"/>
      <stop offset="1" stop-color="#2e2e2e"/>
    </radialGradient>
  </defs>

  <rect class="backdrop-photo" width="925" height="1308" fill="url(#backdrop-tone)" role="img" aria-label="Black and white photo of yoga students stretching in a studio"/>

  <polygon class="accent-top-soft" points="0,0 432,0 0,431" fill="var(--red-soft)" opacity="0.85"/>
  <polygon class="accent-top-deep" points="0,0 8,0 157,276 0,431" fill="var(--red-deep)"/>

  <polygon class="info-panel" points="0,431 157,276 717,1308 0,1308" fill="var(--ink)"/>

  <polygon class="price-corner" points="717,1308 647,1166 925,981 925,1308" fill="var(--red)"/>

  <g class="brand">
    <circle cx="57" cy="541" r="37" fill="var(--white)"/>
    <text class="brand-name" x="105" y="552" font-size="25" fill="var(--white)">Brightfield Athletics and fitness</text>
  </g>

  <g class="headline serif" fill="var(--white)">
    <text x="27" y="663" font-size="74">SPRING RENEWAL</text>
    <text x="27" y="754" font-size="74">YOGA CLASS</text>
  </g>

  <rect class="teacher-band" x="0" y="801" width="560" height="78" fill="var(--red)"/>
  <g class="teacher-note sans" fill="var(--white)" font-size="31">
    <text x="33" y="832" textLength="500" lengthAdjust="spacingAndGlyphs">World-renowned TOBE GARROWEN</text>
    <text x="42" y="870">will be teaching.</text>
  </g>

  <circle class="teacher-portrait" cx="712" cy="844" r="163" fill="url(#portrait-tone)" stroke="var(--red)" stroke-width="5" role="img" aria-label="Portrait photo of the yoga teacher"/>

  <g class="event-date serif" fill="var(--white)">
    <text x="0" y="0" font-size="56" transform="translate(92 1048) rotate(-90)">5th</text>
    <text x="112" y="976" font-size="66">January</text>
    <text x="112" y="1053" font-size="84">2019</text>
  </g>

  <g class="event-time">
    <circle cx="64" cy="1136" r="16" fill="var(--icon-grey)"/>
    <path d="M64 1125 V1137 L72 1143" stroke="var(--ink)" stroke-width="3" fill="none" stroke-linecap="round"/>
    <text class="sans" x="97" y="1152" font-size="42" fill="var(--white)">2pm - 4pm</text>
  </g>

  <g class="event-venue">
    <path d="M62 1244 C55 1234 51 1228 51 1222 A11 11 0 0 1 73 1222 C73 1228 69 1234 62 1244 Z" fill="var(--icon-grey)"/>
    <circle cx="62" cy="1222" r="4" fill="var(--ink)"/>
    <text class="sans" x="92" y="1243" font-size="36" textLength="545" lengthAdjust="spacingAndGlyphs" fill="var(--white)">Brightfield Athletics &amp; Fitness</text>
  </g>

  <g class="event-price serif" fill="var(--white)" text-anchor="middle">
    <text x="789" y="1219" font-size="52">$30 / $40</text>
    <text x="803" y="1256" font-size="34">at the door</text>
  </g>
</svg>
</body>
</html>
```